lab equipment website

We need a fresh new look for a company website called tarvio. We will be using the current logo and brand colors on their current website tarvio.com. They want to keep their text and on-page SEO, but would like to reformat it to look more modern and fresh. They want to have everything be high performance with a great user experience. Their main call to action is for people to fill in a contact form so they can call them. There is some information that is purposely above the fold on the instrument pages. I will need the home page, about page and a leasing page.

```html
<!DOCTYPE html>
<html lang="en">
<head>
<meta charset="utf-8">
<title>tarvio – About</title>
<link href="https://fonts.googleapis.com/css2?family=Montserrat:wght@500;600;700;800&family=Raleway:wght@400;500;600&display=swap" rel="stylesheet">
<style>
:root{
  --teal-dark:#0b6b70;
  --teal:#1fbfa6;
  --navy:#243f4e;
  --navy-text:#2d4a5a;
  --orange:#ff6a00;
  --accent:#f2b705;
  --white:#ffffff;
  --body:#3b3b3b;
  --line:#15616a;
  --ink:#111111;
}
*{margin:0;padding:0;box-sizing:border-box}
html,body{width:818px;height:1200px;overflow:hidden;background:var(--white)}
body{position:relative;font-family:"Raleway",sans-serif;color:var(--body)}
.hero-photo{position:absolute;left:0;top:0;width:818px;height:400px}
.site-header{position:absolute;left:0;top:0;width:818px;height:54px;background:var(--teal-dark);z-index:2}
.brand{position:absolute;left:42px;top:12px;display:flex;align-items:center;gap:6px}
.brand-mark{width:14px;height:14px;background:var(--teal)}
.brand-name{font-family:"Montserrat",sans-serif;font-weight:700;font-size:19px;color:var(--white);line-height:1}
.main-nav a{position:absolute;top:23px;font-family:"Raleway",sans-serif;font-weight:500;font-size:11.5px;color:var(--white);text-decoration:none}
.main-nav a.active{border-bottom:1.5px solid var(--accent);padding-bottom:3px}
.hero-title{position:absolute;left:82px;top:214px;font-family:"Montserrat",sans-serif;font-weight:800;font-size:34px;line-height:31px;color:var(--white);z-index:1}
.hero-sub{position:absolute;left:82px;top:286px;font-size:16px;color:var(--white);z-index:1}
.mission-title{position:absolute;left:0;width:818px;top:398px;text-align:center;font-family:"Montserrat",sans-serif;font-weight:800;font-size:35px;color:var(--navy)}
.rule{position:absolute;height:1.5px;background:var(--line)}
.icon-disc{position:absolute;width:98px;height:98px;border-radius:50%;background:var(--teal)}
.mission-icon{position:absolute;width:98px;height:120px;overflow:visible;fill:none;stroke:var(--ink);stroke-width:2.6;stroke-linejoin:round;stroke-linecap:round}
.mission-text{position:absolute;font-size:11px;line-height:22px;text-align:center;color:var(--body)}
.tagline{position:absolute;left:0;width:818px;top:902px;text-align:center;font-family:"Raleway",sans-serif;font-weight:600;font-size:15.5px;line-height:22px;color:var(--navy-text)}
.cta{position:absolute;left:338px;top:956px;width:144px;height:30px;border-radius:3px;background:var(--orange);color:var(--white);font-family:"Montserrat",sans-serif;font-weight:700;font-size:11px;display:flex;align-items:center;justify-content:center;text-decoration:none}
.footer-wave{position:absolute;left:0;top:1000px;width:818px;height:200px}
.footer-brand{position:absolute;left:93px;top:1076px;display:flex;align-items:center;gap:6px}
.footer-brand .brand-mark{width:13px;height:13px}
.footer-about{position:absolute;left:121px;top:1110px;width:170px;font-size:6px;line-height:8px;color:var(--white)}
.connect{position:absolute;left:600px;width:142px;top:1087px;text-align:center;font-size:13.5px;font-weight:500;color:var(--white)}
.social{position:absolute;width:22px;height:22px;top:1117px}
.social circle.bg{fill:var(--orange)}
.social .glyph{fill:none;stroke:var(--white);stroke-width:1.4;stroke-linecap:round;stroke-linejoin:round}
.footer-nav a{position:absolute;top:1168px;font-size:9px;font-weight:500;color:var(--white);text-decoration:none}
.copyright{position:absolute;left:0;width:818px;top:1188px;text-align:center;font-size:8.5px;font-weight:500;color:var(--white)}
</style>
</head>
<body>
<svg class="hero-photo" viewBox="0 0 818 400" role="img" aria-label="Photo of a cheering team of professionals with raised arms">
  <defs>
    <linearGradient id="heroTone" x1="0" y1="0" x2="1" y2="1">
      <stop offset="0" stop-color="#5f8a99"/>
      <stop offset="0.5" stop-color="#41697c"/>
      <stop offset="1" stop-color="#2d4e60"/>
    </linearGradient>
  </defs>
  <rect width="818" height="400" fill="url(#heroTone)"/>
  <path d="M0 328 C60 380 140 402 208 400 C350 396 480 300 616 304 C700 306 770 340 818 376 L818 400 L0 400Z" fill="#ffffff"/>
</svg>

<header class="site-header">
  <div class="brand"><span class="brand-mark"></span><span class="brand-name">tarvio</span></div>
  <nav class="main-nav">
    <a style="left:273px">Home</a>
    <a class="active" style="left:330px">About</a>
    <a style="left:389px">Leasing</a>
    <a style="left:456px">Contact</a>
    <a style="left:524px">FAQ</a>
  </nav>
</header>

<h1 class="hero-title">YOUR SUCCESS<br>OUR SUPPORT</h1>
<p class="hero-sub">Tarvio is fully dedicated to saving you time and money.</p>

<h2 class="mission-title">TARVIO’S MISSION</h2>

<div class="rule" style="left:448px;width:288px;top:502px"></div>
<div class="icon-disc" style="left:475px;top:453px"></div>
<svg class="mission-icon" style="left:475px;top:453px" viewBox="0 0 98 120" role="img" aria-label="Lab flask icon">
  <rect x="36" y="25" width="26" height="7"/>
  <path d="M40 32 V58 L18 104 H80 L58 58 V32"/>
  <path d="M27 86 q5 -4 10 0 t10 0 t10 0 t10 0 t6 0"/>
</svg>
<p class="mission-text" style="left:176px;width:300px;top:483px">Our mission is to assist laboratories that seek to<br>further scientific innovation.</p>

<div class="rule" style="left:82px;width:296px;top:611px"></div>
<div class="icon-disc" style="left:245px;top:562px"></div>
<svg class="mission-icon" style="left:245px;top:562px" viewBox="0 0 98 120" role="img" aria-label="Wrench and screwdriver icon">
  <path d="M14 28 L20 22 L58 60 L52 66 Z"/>
  <path d="M52 66 L58 60 L86 88 L80 100 L68 94 Z"/>
  <path d="M62 76 L72 66 M68 82 L78 72 M74 88 L82 80"/>
  <path d="M84 30 L30 84 M90 36 L36 90"/>
  <path d="M84 30 C78 24 80 14 88 12 L84 20 L90 26 L98 22 C96 30 92 34 90 36"/>
  <path d="M30 84 C24 84 18 90 20 98 L26 92 L32 96 L30 104 C38 102 40 96 36 90"/>
</svg>
<p class="mission-text" style="left:372px;width:340px;top:583px">By providing equipment leasing and hassle free repair coverage,<br>we aim to accelerate research and relieve laboratories of heavy<br>financial burdens.</p>

<div class="rule" style="left:466px;width:270px;top:720px"></div>
<div class="icon-disc" style="left:479px;top:671px"></div>
<svg class="mission-icon" style="left:479px;top:671px" viewBox="0 0 98 120" role="img" aria-label="Price tag icon">
  <path d="M4 100 L20 116 L80 64 L80 22 L40 24 Z"/>
  <circle cx="68" cy="36" r="6"/>
  <g transform="rotate(-40 44 74)">
    <path d="M52 64 C48 58 36 60 38 68 C40 74 52 72 52 80 C52 88 38 88 36 82"/>
    <path d="M44 56 V92"/>
  </g>
</svg>
<p class="mission-text" style="left:124px;width:348px;top:695px">At the rate that science and technology move, researchers should<br>not be slowed down by inaccessible or unaffordable research<br>equipment.</p>

<div class="rule" style="left:82px;width:274px;top:830px"></div>
<div class="icon-disc" style="left:236px;top:781px"></div>
<svg class="mission-icon" style="left:236px;top:781px" viewBox="0 0 98 120" role="img" aria-label="Thumbs up icon">
  <path d="M10 93 H36 M36 64 V93 H44 V64 Z"/>
  <path d="M44 66 L52 60 L56 42 C57 36 65 36 64 44 L62 58 H86 C94 58 94 68 86 68 C94 68 94 78 86 78 C92 78 92 88 84 88 C90 88 88 96 82 96 H58 L44 90"/>
  <path d="M52 28 L55 34 M60 24 V31 M68 28 L65 34 M44 36 L50 39 M76 36 L70 39 M42 46 L49 46"/>
</svg>
<p class="mission-text" style="left:348px;width:340px;top:803px">Our leasing model stands behind this statement, promising labs<br>financial and operational flexibility.</p>

<p class="tagline">WE ARE TARVIO. ACHIEVE YOUR SUCCESS;<br>COUNT ON OUR SUPPORT.</p>
<a class="cta">VIEW FAQ</a>

<svg class="footer-wave" viewBox="0 0 818 200" aria-hidden="true">
  <path d="M0 44 C200 20 420 0 600 8 C700 12 780 50 818 88 L818 200 L0 200Z" fill="#243f4e"/>
</svg>

<footer>
  <div class="footer-brand"><span class="brand-mark"></span><span class="brand-name">tarvio</span></div>
  <p class="footer-about">We are a team of Halden University scientists driven by our passion for research. We strive to serve the scientific community. We love what we do, and who we work with. Together we can make positive changes in the world of research.</p>
  <p class="connect">Connect With Us</p>
  <svg class="social" style="left:619px" viewBox="0 0 22 22" role="img" aria-label="Email">
    <circle class="bg" cx="11" cy="11" r="11"/>
    <rect class="glyph" x="6" y="7.5" width="10" height="7"/><path class="glyph" d="M6 7.5 L11 11.5 L16 7.5"/>
  </svg>
  <svg class="social" style="left:647px" viewBox="0 0 22 22" role="img" aria-label="Phone">
    <circle class="bg" cx="11" cy="11" r="11"/>
    <path class="glyph" d="M7.5 6 L9.5 6 L10.5 8.5 L9.3 9.5 C10 11 11 12 12.5 12.7 L13.5 11.5 L16 12.5 L16 14.5 C11 15 7 11 7.5 6 Z"/>
  </svg>
  <svg class="social" style="left:674px" viewBox="0 0 22 22" role="img" aria-label="Location">
    <circle class="bg" cx="11" cy="11" r="11"/>
    <path class="glyph" d="M11 17 C8 13.5 7 11.5 7 9.5 A4 4 0 0 1 15 9.5 C15 11.5 14 13.5 11 17 Z"/><circle class="glyph" cx="11" cy="9.5" r="1.4"/>
  </svg>
  <svg class="social" style="left:701px" viewBox="0 0 22 22" role="img" aria-label="Website">
    <circle class="bg" cx="11" cy="11" r="11"/>
    <circle class="glyph" cx="11" cy="11" r="5"/><path class="glyph" d="M6 11 H16 M11 6 C9 8.5 9 13.5 11 16 M11 6 C13 8.5 13 13.5 11 16"/>
  </svg>
  <nav class="footer-nav">
    <a style="left:518px">Home</a>
    <a style="left:565px">About</a>
    <a style="left:611px">Leasing</a>
    <a style="left:665px">Contact</a>
    <a style="left:720px">FAQ</a>
  </nav>
  <p class="copyright">Tarvio © | 2018 | All Rights Reserved.</p>
</footer>
</body>
</html>
```